INNOVATIVE DESIGN NEEDED FOR FINANCIAL COMPANY

INTERNATIONAL FIRM IN HONG KONG NEEDS A MODERN BUSINESS CARD DESIGN. ONE SIDE ENGLISH OTHER SIDE IN CHINESE. WE ARE OPEN TO CHANGING FONTS AND COLOR. SHOULD BE A CARD THAT IS PROFESSIONAL DEALING WITH HIGH NET WORTH CLIENTELE. BOTH SIDES OF THE CARD WILL BE THE SAME, HOWEVER, THE WORDING ON ONE SIDE WILL BE ENGLISH AND THE OTHER SIDE IN CHINESE (CAN ASSIST IN THE LETTERING - CAN PROVIDE ONCE CARD DESIGN IS ACCEPTED.

Target Market(s)

Hong Kong/CHINA

Contact Information for Business Card

ATTRACTIVE MODERN

```html
<!DOCTYPE html>
<html lang="en">
<head>
<meta charset="utf-8">
<title>Cedarline Asset Management – Business Card</title>
<link rel="stylesheet" href="https://fonts.googleapis.com/css2?family=Arimo:wght@400;700&family=Noto+Sans+TC:wght@900&family=Roboto+Slab:wght@800&display=swap">
<style>
  :root {
    --backdrop: #e9e9e6;
    --card: #f7f7f6;
    --brand-green: #14a884;
    --brand-green-light: #17bf96;
    --bar-grey: #48484b;
    --ink-dark: #4b4b4d;
    --ink-mid: #8a8a8c;
    --white: #ffffff;
  }
  * { box-sizing: border-box; margin: 0; padding: 0; }
  html, body {
    width: 1200px; height: 780px; overflow: hidden;
    background: var(--backdrop);
  }
  .canvas {
    position: relative; width: 1200px; height: 780px;
    display: flex; align-items: center; justify-content: center;
  }
  .card {
    position: relative; width: 980px; height: 560px;
    background: linear-gradient(160deg, var(--white), var(--card));
    overflow: hidden;
    box-shadow: 0 10px 30px rgba(0,0,0,.18);
  }
  .brand-disc {
    position: absolute; left: 660px; top: 30px;
    width: 400px; height: 400px; border-radius: 50%;
    background: var(--brand-green);
  }
  .name-bar {
    position: absolute; left: 240px; top: 262px; width: 520px; height: 64px;
    background: var(--bar-grey);
    display: flex; align-items: center; padding-left: 40px;
    font-family: "Arimo", Arial, sans-serif; color: var(--white);
  }
  .name-bar .person { font-size: 31px; font-weight: 700; }
  .name-bar .divider { font-size: 30px; margin: 0 10px; opacity: .85; }
  .name-bar .role { font-size: 24px; }
  .contact-band {
    position: absolute; left: 240px; top: 326px; right: 0; bottom: 0;
    background: linear-gradient(180deg, var(--brand-green-light), var(--brand-green));
    padding: 28px 0 0 40px;
    font-family: "Arimo", Arial, sans-serif; color: var(--white);
  }
  .contact-band p { font-size: 22px; line-height: 33px; }
  .contact-line { display: flex; align-items: center; gap: 14px; }
  .contact-line svg { width: 20px; height: 20px; flex: none; }
  .address { margin-bottom: 6px; }
  .marker {
    position: absolute; left: 62px; top: 300px;
    width: 112px; height: 112px; border-radius: 50%;
    background: var(--brand-green);
  }
  .company {
    position: absolute; left: 130px; top: 96px; width: 500px;
  }
  .company-zh {
    font-family: "Noto Sans TC", sans-serif; font-weight: 900;
    font-size: 45px; line-height: 1.2; color: var(--ink-dark); letter-spacing: 3px;
    white-space: nowrap;
  }
  .company-en {
    font-family: "Roboto Slab", serif; font-weight: 800;
    font-size: 18px; color: var(--ink-mid); letter-spacing: 3px;
    margin-top: 6px; white-space: nowrap;
  }
</style>
</head>
<body>
<main class="canvas">
  <section class="card">
    <div class="brand-disc"></div>

    <header class="company">
      <h1 class="company-zh">雪松資產管理有限公司</h1>
      <p class="company-en">Cedarline Asset Management Ltd</p>
    </header>

    <div class="marker"></div>

    <div class="name-bar">
      <span class="person">Daniel Hartley</span>
      <span class="divider">|</span>
      <span class="role">Director</span>
    </div>

    <div class="contact-band">
      <div class="address">
        <p>PO Box 48, Harbour Road</p>
        <p>Wan Chai, Hong Kong</p>
      </div>
      <p class="contact-line">
        <svg viewBox="0 0 20 20" aria-hidden="true"><rect x="2" y="2" width="16" height="16" fill="none" stroke="#fff" stroke-width="2"/></svg>
        (852) 2380 4417
      </p>
      <p class="contact-line">
        <svg viewBox="0 0 20 20" aria-hidden="true"><rect x="1" y="4" width="18" height="12" fill="#fff"/><path d="M1 4 L10 11 L19 4" fill="none" stroke="#14a884" stroke-width="1.6"/></svg>
        info@cedarlineam.com
      </p>
      <p class="contact-line">
        <svg viewBox="0 0 20 20" aria-hidden="true"><circle cx="10" cy="10" r="8.5" fill="#fff"/><path d="M1.5 10 H18.5 M10 1.5 V18.5 M10 1.5 C5 6 5 14 10 18.5 M10 1.5 C15 6 15 14 10 18.5" fill="none" stroke="#14a884" stroke-width="1.2"/></svg>
        www.cedarlineam.com
      </p>
    </div>
  </section>
</main>
</body>
</html>
```